Bravo Lendmart
The Loan Exchange Platform
Bravo Lendmart -
Creative Brief
Www.bravolendmart.example
Bravo Lendmart is going to launch as a platform to connect buyers and sellers of high quality Credit Union originated loans. We will be offering commercial loans at the outset, but will quickly add other types of loans through the exchange. Our platform will streamline the process of loan sales and participations between financial institutions. Weare partnering with www.notequay.example and their software will power our exchange.
See www.fenpoint.example for an example of what we like. We're looking for a design that will include placeholders for future RSS feeds, flash, and industry news. We will need a banner at the top that reads "Bravo Lendmart (our logo) - powered by NoteQuay (their logo)". The NoteQuay logo is on their website - www.notequay.example . Above all, we was tittle modern, welcoming, and NOT intimidating. Our logo design is included below. Colors should include those in our logo.
Masculine
See logo
top
Www.fenpoint.example
Www.notequay.example
http://orders.markforge.example/contests/bravolendmart-online-loan-participation-exchange
We just selected our logo on this site. Please refer to submission #28. http://orders.markforge.example/contests/bravolendmart-online-loan-participation-exchange

```html
<!DOCTYPE html>
<html lang="en">
<head>
<meta charset="utf-8">
<title>Bravo Lendmart – The Loan Exchange Platform</title>
<link rel="stylesheet" href="https://fonts.googleapis.com/css2?family=Arimo:wght@400;700&display=swap">
<style>
:root{
  --teal:#1aaed3;
  --teal-dark:#0b8fb3;
  --navy:#0b3d6e;
  --blue-btn:#1a6fb5;
  --green:#5aa51f;
  --green-dark:#3f7f12;
  --red:#d0262b;
  --ink:#333a40;
  --muted:#6b737a;
  --panel-line:#cfd4d8;
  --page:#eef0f1;
  --white:#ffffff;
}
*{box-sizing:border-box;margin:0;padding:0}
html,body{width:1200px;height:1028px;overflow:hidden}
body{position:relative;background:var(--page);font-family:"Arimo",Arial,sans-serif;color:var(--ink)}
.abs{position:absolute}

.site-header{left:0;top:0;width:1200px;height:125px;background:var(--white)}
.teal-band{left:0;top:125px;width:1200px;height:335px;background:linear-gradient(180deg,var(--teal) 0%,#2fc0e0 70%,#8fdcef 100%)}

.topbar{top:10px;left:640px;display:flex;align-items:center;gap:14px;font-size:13px;color:var(--ink)}
.topbar .date{font-weight:700;font-size:12px}
.login-btn{background:var(--blue-btn);color:var(--white);font-size:12px;font-weight:700;padding:4px 12px;border-radius:3px}
.topbar .sep{color:var(--panel-line)}

.brand{left:190px;top:38px;display:flex;align-items:center;gap:10px}
.brand .mark{width:28px;height:28px;border-radius:50%;background:var(--green)}
.brand .name{font-size:40px;font-weight:700;color:var(--navy);letter-spacing:-0.5px;white-space:nowrap}

.contact-lines{left:850px;top:44px;font-size:12px;color:var(--ink);line-height:26px}
.contact-lines div{display:flex;align-items:center;gap:6px;white-space:nowrap}
.contact-lines b{font-weight:700}

.main-nav{left:478px;top:100px;display:flex;gap:4px}
.main-nav a{display:block;height:26px;line-height:26px;padding:0 22px;background:linear-gradient(180deg,#6fbf2c,var(--green-dark));color:var(--white);font-size:13px;font-weight:700;text-decoration:none;border-radius:3px 3px 0 0;white-space:nowrap}

.hero{left:183px;top:125px;width:822px;height:333px;background:var(--white);box-shadow:0 6px 18px rgba(0,0,0,.25)}
.hero-photo{left:22px;top:28px;width:420px;height:264px;border:4px solid #e2e6e8;background:linear-gradient(135deg,#dfe6ea 0%,#a9b8c2 45%,#5f7482 100%)}
.slider-dots{left:180px;top:306px;display:flex;gap:8px}
.slider-dots span{width:9px;height:9px;border-radius:50%;background:#3a4046}
.slider-dots span.on{background:var(--teal)}
.partner-block{left:470px;top:70px;width:330px;text-align:center}
.partner-block .brand-line{display:flex;align-items:center;justify-content:center;gap:10px}
.partner-block .brand-line .mark{width:26px;height:26px;border-radius:50%;background:var(--green)}
.partner-block .brand-line .name{font-size:38px;font-weight:700;color:var(--navy);white-space:nowrap}
.powered{margin-top:26px;font-size:20px;font-weight:700;color:var(--red);letter-spacing:1px}
.partner-name{margin-top:14px;font-size:42px;font-weight:700;color:var(--navy)}
.partner-tag{margin-top:4px;font-size:11px;color:var(--muted);letter-spacing:2px}

.content-panel{left:183px;top:500px;width:822px;height:418px;background:var(--white);border:1px solid var(--panel-line);border-radius:16px}

.box{border:1px solid var(--panel-line);background:var(--white)}
.box-title{font-size:17px;font-weight:700;color:var(--navy);text-align:center;padding:12px 0 8px;white-space:nowrap}

.welcome{left:211px;top:528px;width:212px;height:306px}
.welcome .box-title{font-size:14px;padding:14px 0 10px}
.welcome-img{margin:0 6px;height:116px;background:linear-gradient(135deg,#7c8388,#2f3438 60%,#555c61)}
.welcome p{font-size:10px;line-height:14px;color:var(--muted);padding:10px 8px 0}
.read-more{left:118px;top:262px;background:var(--green);color:var(--white);font-size:12px;font-weight:700;padding:6px 10px;border-radius:2px}

.news{left:459px;top:528px;width:214px;height:306px}
.news .box-title{border-bottom:1px solid var(--panel-line);margin:0 10px}
.news-item{display:flex;gap:10px;padding:14px 14px 0 18px}
.news-date{width:36px;text-align:center;flex:none}
.news-date .day{background:var(--green);color:var(--white);font-weight:700;font-size:17px;height:30px;line-height:30px}
.news-date .mon{font-size:13px;color:var(--ink);margin-top:3px}
.news-text{font-size:10px;line-height:13px;color:var(--muted)}
.news-text em{font-style:normal;color:var(--green);font-weight:700}
.see-all{left:24px;top:278px;font-size:11px;font-weight:700;color:var(--ink)}

.connect{left:706px;top:528px;width:299px;height:310px;background:#f6f8f9}
.connect-head{height:42px;background:var(--navy);color:var(--white);font-size:17px;text-align:center;line-height:42px}
.signin{margin:12px 14px 0;background:var(--white);border:1px solid var(--panel-line);padding:10px 10px 8px}
.signin h3{font-size:14px;font-weight:700;color:var(--navy);padding-bottom:6px;border-bottom:1px solid var(--panel-line);margin-bottom:8px}
.field{display:flex;align-items:center;justify-content:space-between;font-size:11px;margin-bottom:6px}
.field span.input{width:160px;height:18px;border:1px solid #9aa3aa;background:var(--white)}
.forgot{font-size:10px;color:var(--ink);margin:2px 0 6px}
.remember{display:flex;align-items:center;justify-content:space-between;font-size:11px}
.remember label{display:flex;align-items:center;gap:6px}
.remember .box-check{width:11px;height:11px;border:1px solid #7a848b;background:var(--white)}
.signin-btn{background:var(--blue-btn);color:var(--white);font-weight:700;font-size:11px;padding:4px 12px;border-radius:2px}
.social{display:flex;justify-content:center;gap:28px;margin-top:14px}
.social span{width:46px;height:46px;border-radius:12px}
.social .s1{background:#3b5c9a}
.social .s2{background:#f08a24}
.social .s3{background:#4cb8e8}

.site-footer{left:0;top:945px;width:1200px;height:83px;background:linear-gradient(180deg,var(--teal),var(--teal-dark));color:var(--white);text-align:center}
.footer-nav{margin-top:22px;font-size:13px;display:flex;justify-content:center;gap:12px}
.footer-nav .sep{opacity:.7}
.copyright{margin-top:16px;font-size:12px}
</style>
</head>
<body>

<header class="site-header abs">
  <div class="topbar abs">
    <span class="date">Saturday, February 11, 2012</span>
    <span class="login-btn">Log In</span>
    <span class="sep">|</span><span>Subscribe</span>
    <span class="sep">|</span><span>Contact Us</span>
  </div>

  <div class="brand abs">
    <span class="mark"></span>
    <span class="name">Bravo Lendmart</span>
  </div>

  <div class="contact-lines abs">
    <div>
      <svg width="16" height="16" viewBox="0 0 16 16"><path d="M4 1h3l1 4-2 1c1 2 2 3 4 4l1-2 4 1v3c0 1-1 2-2 2C7 14 2 9 2 3c0-1 1-2 2-2z" fill="#333a40"/></svg>
      <span><b>Toll Free :</b> 800.555.0147</span>
    </div>
    <div>
      <svg width="16" height="16" viewBox="0 0 16 16"><rect x="1" y="3" width="14" height="10" rx="1" fill="#333a40"/><path d="M1 4l7 5 7-5" stroke="#fff" stroke-width="1.3" fill="none"/></svg>
      <span><b>E-mail :</b> support@bravolendmart.example</span>
    </div>
  </div>

  <nav class="main-nav abs">
    <a>Home</a><a>About Us</a><a>Certification</a><a>The Xchange</a><a>Info Request</a>
  </nav>
</header>

<div class="teal-band abs"></div>

<section class="hero abs">
  <div class="hero-photo abs" role="img" aria-label="Photo of two business professionals reviewing loan documents at a desk"></div>
  <div class="slider-dots abs"><span class="on"></span><span></span><span></span><span></span><span></span></div>
  <div class="partner-block abs">
    <div class="brand-line"><span class="mark"></span><span class="name">Bravo Lendmart</span></div>
    <div class="powered">POWERED BY</div>
    <div class="partner-name">NoteQuay</div>
    <div class="partner-tag">THE NOTE EXCHANGE</div>
  </div>
</section>

<div class="content-panel abs"></div>

<section class="welcome box abs">
  <h2 class="box-title">Welcome to Bravo Lendmart</h2>
  <div class="welcome-img" role="img" aria-label="Image of interlocking machine gears"></div>
  <p>Looking to diversify your business loan portfolio by selling off concentrations or buying quality loans from peers? Meet trusted participants and close faster. Are you ready to join?</p>
  <span class="read-more abs">Read More</span>
</section>

<section class="news box abs">
  <h2 class="box-title">Industry News</h2>
  <div class="news-item">
    <div class="news-date"><div class="day">12</div><div class="mon">Feb</div></div>
    <div class="news-text">New loan pools listed for member credit unions today.<br><em>More »</em></div>
  </div>
  <div class="news-item">
    <div class="news-date"><div class="day">11</div><div class="mon">Feb</div></div>
    <div class="news-text">Pricing update released for commercial participations this week.<br><em>More »</em></div>
  </div>
  <div class="news-item">
    <div class="news-date"><div class="day">10</div><div class="mon">Feb</div></div>
    <div class="news-text">Webinar set on streamlining loan sales between institutions.<br><em>More »</em></div>
  </div>
  <span class="see-all abs">See all</span>
</section>

<section class="connect box abs">
  <div class="connect-head">Connect With Us</div>
  <div class="signin">
    <h3>Sign In</h3>
    <div class="field"><span>Institution ID :</span><span class="input"></span></div>
    <div class="field"><span>User ID :</span><span class="input"></span></div>
    <div class="field"><span>Password :</span><span class="input"></span></div>
    <div class="forgot">Forgot My Institution and User ID ?</div>
    <div class="remember">
      <label><span class="box-check"></span>Remember Me</label>
      <span class="signin-btn">Sign In</span>
    </div>
  </div>
  <div class="social"><span class="s1"></span><span class="s2"></span><span class="s3"></span></div>
</section>

<footer class="site-footer abs">
  <div class="footer-nav">
    <span>Home</span><span class="sep">|</span><span>About Us</span><span class="sep">|</span><span>Certification</span><span class="sep">|</span><span>The Xchange</span><span class="sep">|</span><span>Info Request</span><span class="sep">|</span><span>Subscribe</span><span class="sep">|</span><span>Contact Us</span>
  </div>
  <div class="copyright">Bravo Lendmart © 2012 &nbsp;|&nbsp; Privacy Policy</div>
</footer>

</body>
</html>
```